RWT Installations Ltd Business Cards

We need a business card with our business logo. We provide window and door installations on high-rises in west coast British Colombia, Canada.

I would like my business information and details on one side of the card, and the other side the company name with logo

Target Market(s)

General Contractors

Industry/Entity Type

Construction

Contact Information for Business Card

one side i want my company name and logo in the dark theme logo that i provided

Requirements
Must have
• Tomas Verelund, 15559284016, RWTInstallations@mailvera.example, 1408-5192 Pellow Avenue Burnaby BC, V0X 1Z9, Owner & Manager

```html
<!DOCTYPE html>
<html lang="en">
<head>
<meta charset="UTF-8">
<title>RWT Installations Ltd – Business Cards</title>
<link rel="stylesheet" href="https://fonts.googleapis.com/css2?family=Montserrat:wght@400;500;700&display=swap">
<style>
  :root {
    --page-bg: #e6e6e4;
    --card-dark: #3a3a3a;
    --card-dark-edge: #2a2a2a;
    --card-light: #ffffff;
    --accent: #2f9be8;
    --accent-light: #3cc3f0;
    --ink: #2b2b2b;
    --ink-soft: #555555;
    --rule: #3a3a3a;
  }
  * { margin: 0; padding: 0; box-sizing: border-box; }
  html, body { width: 1200px; height: 900px; overflow: hidden; }
  body {
    background: var(--page-bg);
    font-family: "Montserrat", sans-serif;
    position: relative;
  }
  .card {
    position: absolute;
    left: 260px;
    width: 680px;
    height: 388px;
    border-radius: 22px;
    overflow: hidden;
    box-shadow: 0 10px 28px rgba(0,0,0,0.22);
  }
  .card-front {
    top: 44px;
    background: linear-gradient(135deg, #454545 0%, var(--card-dark) 55%, var(--card-dark-edge) 100%);
  }
  .card-back {
    top: 468px;
    background: linear-gradient(135deg, #454545 0%, var(--card-dark) 55%, var(--card-dark-edge) 100%);
  }
  .brand {
    position: absolute;
    display: flex;
    align-items: center;
    gap: 14px;
  }
  .card-front .brand { left: 50%; top: 50%; transform: translate(-50%, -50%); }
  .card-back .brand { left: 34px; top: 50%; transform: translateY(-50%); }
  .brand-mark {
    width: 34px; height: 34px;
    background: var(--accent-light);
  }
  .card-back .brand-mark { width: 24px; height: 24px; }
  .brand-name {
    font-weight: 700;
    color: var(--accent-light);
    font-size: 30px;
    letter-spacing: 0.5px;
    white-space: nowrap;
  }
  .card-back .brand-name { font-size: 19px; }
  .back-panel {
    position: absolute;
    inset: 0;
  }
  .contact {
    position: absolute;
    left: 356px;
    top: 0;
    right: 0;
    bottom: 0;
  }
  .person-name {
    position: absolute;
    left: 18px; top: 52px;
    font-size: 27px;
    font-weight: 700;
    color: var(--accent);
    letter-spacing: 0.5px;
  }
  .person-role {
    position: absolute;
    left: 26px; top: 88px;
    font-size: 15px;
    color: var(--ink-soft);
  }
  .contact-line {
    position: absolute;
    left: 30px;
    font-size: 15px;
    color: var(--ink);
    line-height: 1.3;
  }
  .line-phone { top: 150px; }
  .line-email { top: 195px; }
  .line-address { top: 238px; }
  .rule {
    position: absolute;
    left: 20px; right: 36px;
    height: 1px;
    background: var(--rule);
  }
  .rule-1 { top: 142px; }
  .rule-2 { top: 184px; }
  .rule-3 { top: 228px; }
</style>
</head>
<body>

  <section class="card card-front" aria-label="Card front">
    <div class="brand">
      <span class="brand-mark"></span>
      <span class="brand-name">RWT Installations Ltd</span>
    </div>
  </section>

  <section class="card card-back" aria-label="Card back">
    <div class="brand">
      <span class="brand-mark"></span>
      <span class="brand-name">RWT Installations Ltd</span>
    </div>

    <svg class="back-panel" width="680" height="388" viewBox="0 0 680 388">
      <path d="M300 0 H680 V388 H320 C320 360 318 340 330 320 C342 300 350 290 350 270 V118 C350 98 342 88 330 70 C316 50 300 36 300 0 Z" fill="var(--card-light)"/>
      <path d="M300 0 C300 36 316 50 330 70 C336 78 340 84 343 90" fill="none" stroke="var(--accent)" stroke-width="7"/>
      <path d="M343 298 C340 306 336 312 330 320 C318 340 320 360 320 388" fill="none" stroke="var(--accent)" stroke-width="7"/>

      <g class="icon icon-phone" transform="translate(350 160)">
        <circle r="13" fill="var(--accent)"/>
        <path d="M-5 -6 C-6 -1 -2 5 4 7 L6 4 L3 2 L1 3 C-1 2 -3 0 -3 -2 L-2 -4 L-4 -7 Z" fill="#fff"/>
      </g>
      <g class="icon icon-mail" transform="translate(350 204)">
        <circle r="13" fill="var(--accent)"/>
        <rect x="-7" y="-5" width="14" height="10" fill="#fff"/>
        <path d="M-7 -5 L0 1 L7 -5" fill="none" stroke="var(--accent)" stroke-width="1.4"/>
      </g>
      <g class="icon icon-pin" transform="translate(350 248)">
        <circle r="13" fill="var(--accent)"/>
        <path d="M0 8 C-5 2 -6 -1 -6 -3 A6 6 0 0 1 6 -3 C6 -1 5 2 0 8 Z" fill="#fff"/>
        <circle cy="-3" r="2.2" fill="var(--accent)"/>
      </g>
    </svg>

    <div class="contact">
      <h1 class="person-name">TOMAS VERELUND</h1>
      <p class="person-role">Owner &amp; Manager</p>
      <span class="rule rule-1"></span>
      <p class="contact-line line-phone">+1 555 928 4016</p>
      <span class="rule rule-2"></span>
      <p class="contact-line line-email">RWTInstallations@mailvera.example</p>
      <span class="rule rule-3"></span>
      <p class="contact-line line-address">1408-5192 Pellow Avenue<br>Burnaby BC, V0X 1Z9</p>
    </div>
  </section>

</body>
</html>
```